Consulting Firm stationery design

Now that the MakerHive has given us a new logo we'll now need to have all our stationery designed. So we're asking for this community to help us once again.We're looking to get from you Letterheads (Header and Footer, suitable to be applied on a .docx format. Vectors are required but keep this in mind), Envelopes (Front and Back designs, back is not a must but desirable depending on your design), 9"x 12" Pocket Folders (consider design for front and back, also for pockets as well), Business Cards.An elegant design is a must have, mostly for Folders and Envelopes. The idea with this two is to stand out from others when they're handed over. Ideas are welcomed, we were thinking maybe on some texturing simulation for these.Folders will have 3 addresses and contact information. Envelopes will have 1 address and contact information.Brand Manual attached. vendaluxo logo has been copyrighted already. I'm also attaching the current stationary designs (these never got to be out for production but was going to be before we made the brand changes); Pocker folders page 1 to 4 (pages 2 and 4 are the pocket designs), Pages 5 and 6 (6 is the back of the envelope), Pages 7 and 8 (8 is the back of the business card). No letterhead within these designs as it just had the logo and address.

Industry/Entity Type

Business Consultant

Font styles to use
Serif
Sans Serif

Requirements
Must have
• Elegance
Nice to have
• Modern looking out of common

```html
<!DOCTYPE html>
<html lang="en">
<head>
<meta charset="utf-8">
<title>vendaluxo letterhead</title>
<link rel="stylesheet" href="https://fonts.googleapis.com/css2?family=PT+Sans:wght@400;700&family=Montserrat:wght@400;700&display=swap">
<style>
  :root {
    --backdrop: #b8c5cb;
    --paper: #ffffff;
    --brand-blue: #2f88e0;
    --brand-blue-deep: #1f6fc4;
    --ink: #111418;
    --logo-ink: #1c2230;
  }
  * { box-sizing: border-box; margin: 0; padding: 0; }
  html, body {
    width: 1200px;
    height: 800px;
    overflow: hidden;
    background: var(--backdrop);
  }
  .canvas {
    position: relative;
    width: 1200px;
    height: 800px;
  }
  .letterhead {
    position: absolute;
    left: 315px;
    top: 20px;
    width: 570px;
    height: 760px;
    background: var(--paper);
    overflow: hidden;
  }
  .letterhead__bands {
    position: absolute;
    inset: 0;
    width: 570px;
    height: 760px;
  }
  .brand-name {
    position: absolute;
    right: 56px;
    top: 40px;
    display: flex;
    align-items: center;
    gap: 8px;
    font-family: "PT Sans", sans-serif;
    font-weight: 700;
    font-size: 30px;
    letter-spacing: 0.5px;
    color: var(--logo-ink);
  }
  .brand-name__dot {
    width: 14px;
    height: 14px;
    border-radius: 50%;
    background: var(--brand-blue);
  }
  .letter-body {
    position: absolute;
    left: 57px;
    top: 158px;
    width: 457px;
    font-family: "PT Sans", sans-serif;
    font-size: 12.6px;
    line-height: 16.9px;
    color: var(--ink);
    text-align: justify;
    hyphens: auto;
  }
  .letter-body p { margin-bottom: 16.9px; }
  .contact-block {
    position: absolute;
    left: 57px;
    top: 663px;
    font-family: "Montserrat", sans-serif;
    font-size: 16.5px;
    line-height: 20.3px;
    color: var(--ink);
  }
</style>
</head>
<body>
<main class="canvas">
  <article class="letterhead">
    <svg class="letterhead__bands" viewBox="0 0 676 900" preserveAspectRatio="none" aria-hidden="true">
      <path d="M0 0 H337 L268 68 Q255 79 232 79 H0 Z" fill="var(--brand-blue)"/>
      <path d="M0 0 H312 L262 48 Q252 56 232 56 H0 Z" fill="var(--brand-blue-deep)" opacity="0.35"/>
      <path d="M0 0 H310 L262 46 Q252 54 232 54 H0 Z" fill="var(--brand-blue)"/>
      <path d="M332 900 L395 845 Q410 833 432 833 H676 V900 Z" fill="var(--brand-blue)"/>
      <path d="M372 900 L418 862 Q430 852 450 852 H676 V900 Z" fill="var(--brand-blue-deep)" opacity="0.35"/>
      <path d="M376 900 L420 864 Q432 855 452 855 H676 V900 Z" fill="var(--brand-blue)"/>
    </svg>

    <div class="brand-name"><span>vendaluxo</span><span class="brand-name__dot"></span></div>

    <section class="letter-body">
      <p>Lorem ipsum dolor sit amet,</p>
      <p>Lorem ipsum dolor sit amet, consectetur adipiscing elit. Donec orci purus, luctus vitae dignissim eu, iaculis sed purus. Vivamus faucibus, ipsum nec aliquet viverra, leo mauris condimentum ligula, sit amet sagittis enim ligula quis arcu. Nam egestas tortor id nisi porttitor mattis. In tortor ante, ultricies in suscipit a, tempus non massa. Vivamus et auctor mi. Fusce vel massa nulla. Phasellus nec eros mauris, et scelerisque orci. Donec malesuada orci vitae nulla accumsan porta a id massa. Quisque accumsan iaculis magna sit amet fringilla. Maecenas consequat, magna eget tincidunt semper, odio nibh rutrum mi, id feugiat ante nisi eu risus. Vestibulum nunc orci, rhoncus a placerat in, ultricies in mi. Cras mattis varius eros, vel fringilla nisi suscipit eget.</p>
      <p>Quisque scelerisque sagittis nulla at porttitor. Mauris a justo et tellus interdum tristique. Sed id augue vitae urna euismod commodo aliquet a quam. Pellentesque arcu velit, cursus et malesuada ut, consequat et diam. Nullam erat sem, rhoncus id ullamcorper vitae, rhoncus et arcu. In ultricies ultricies nulla, ut rutrum nisi iaculis at. Donec eu magna a metus ornare faucibus. Fusce aliquet faucibus ultricies. Morbi semper, est id tincidunt gravida, sem arcu adipiscing lacus, ac bibendum nulla leo eu purus. Quisque nec diam sed risus consectetur a ccumsan quis quis nibh. Vestibulum id purus lorem.</p>
      <p>Vivamus vehicula accumsan lacinia. Aliquam erat volutpat. Pellentesque consequat venenatis velit non gravida. Etiam et sem et nulla congue aliquam sed eget augue. Nulla facilisi. Pellentesque habitant morbi tristique senectus et netus et malesuada fames ac turpis egestas. Nulla a elit at sem iaculis congue. Nullam mollis tristique lobortis.</p>
    </section>

    <address class="contact-block" style="font-style: normal;">
      <div>(809) 555 0142</div>
      <div>marta@vendaluxo.do</div>
      <div>www.vendaluxo.do</div>
    </address>
  </article>
</main>
</body>
</html>
```